CrestHornSupply.com

I need a new webdesign for a company in the San Jose/SF Bay area that showcases the financial benefits of buying used band instruments for junior high students.This would be opposed to the current and costly option of renting cheap quality instruments from the 2 or 3 local music stores that charge a monthly fee that over the years charges the buyer 3 or 4x over..
Instruments: focus in on Alto Sax, Trumpet, Flute, Clarinet, Trombone, Tenor Sax, Baritone
Target middle schools are Willowmere Middle School and Harlan Middle School in San Jose, CA. Both have award winning band programs.
Files attached may or may not be important.
Tabs Needed and funtional
Contact
Shopping Cart
Select Instrument
Checkout
Add to Cart, etc.
Instuments
quantity, etc.
trade in your instrument/sell your instrument
ability to add or take away new instruments for sale. including pictures
Additional questions or info, feel free to ask
Updates
Hi Designers,
Project Deadline Extended
Reason: In the next week you will be receiving specific content that will be required to be had on the website.
New desigins are still welcome. Please continue to contact me if you have questions about your individual designs.
Thanks!
Crest Horn

```html
<!DOCTYPE html>
<html lang="en">
<head>
<meta charset="utf-8">
<title>Crest Horn Instruments</title>
<link href="https://fonts.googleapis.com/css2?family=Questrial&family=Open+Sans:wght@400;600;700&family=Josefin+Slab:wght@400;600&display=swap" rel="stylesheet">
<style>
:root{
  --yellow-top:#ffe100;
  --yellow-bottom:#e8a800;
  --ink:#1a1a1a;
  --grey-text:#666;
  --red:#e0141b;
  --title-red:#c8202a;
  --panel:#f4f4f4;
  --icon-grey:#6e6e6e;
  --icon-light:#d9d9d9;
  --card-dark:#3b3b3b;
  --footer:#222;
  --footer-field:#3a3a3a;
  --footer-text:#8c8c8c;
  --star:#f39c12;
}
*{box-sizing:border-box;margin:0;padding:0}
html,body{width:884px;height:1200px;overflow:hidden;background:#fff}
body{position:relative;font-family:'Open Sans',sans-serif;color:var(--ink)}
.abs{position:absolute}

/* header */
.site-header{left:0;top:0;width:884px;height:80px;background:linear-gradient(var(--yellow-top),var(--yellow-bottom));box-shadow:0 2px 4px rgba(0,0,0,.25)}
.brand{left:366px;top:22px;width:174px;text-align:center;font-family:'Questrial',sans-serif;color:var(--ink)}
.brand .l1{font-size:21px;line-height:22px;letter-spacing:.3px}
.brand .l2{font-size:24px;line-height:24px}
.nav a{position:absolute;top:48px;font-family:'Questrial',sans-serif;font-size:13px;color:var(--ink);text-decoration:none}
.account{left:601px;top:19px;font-size:8px;font-weight:600}
.cart-icon{left:682px;top:12px}

/* hero */
.hero-side{top:82px;height:280px;width:126px}
.hero-side.left{left:0;background:radial-gradient(ellipse 70px 110px at 35% 45%,rgba(120,120,120,.45),rgba(255,255,255,0) 100%),#fff}
.hero-side.right{left:758px;background:radial-gradient(ellipse 70px 120px at 65% 40%,rgba(90,90,90,.5),rgba(255,255,255,0) 100%),#fff}
.hero-photo{left:126px;top:82px;width:631px;height:259px;
  background:
    radial-gradient(ellipse 120px 100px at 75% 80%,rgba(140,50,30,.55),transparent 100%),
    radial-gradient(ellipse 90px 110px at 27% 45%,rgba(190,190,190,.35),transparent 100%),
    linear-gradient(100deg,#555 0%,#6b6b6b 30%,#8a8a8a 46%,#2a2a2a 49%,#3a3a3a 70%,#2c2c2c 100%)}
.hero-shadow{left:150px;top:341px;width:590px;height:14px;background:radial-gradient(ellipse at 50% 0,rgba(0,0,0,.25),transparent 70%)}
.slider-arrow{width:30px;height:30px;border-radius:50%;background:radial-gradient(circle at 40% 35%,#ffe14a,#d89b00);border:2px solid #fff;box-shadow:0 1px 3px rgba(0,0,0,.4)}

/* welcome */
.welcome{left:0;top:361px;width:884px;height:184px;background:var(--panel)}
.welcome h1{position:absolute;left:0;top:14px;width:884px;text-align:center;font-family:'Questrial',sans-serif;font-weight:400;font-size:21px;color:#444}
.welcome h1 span{color:var(--title-red)}
.feature-circle{width:72px;height:72px;border-radius:50%;background:var(--icon-grey);box-shadow:0 0 0 2px #e4e4e4}
.welcome p{position:absolute;left:168px;top:135px;width:548px;text-align:center;font-family:'Questrial',sans-serif;font-size:10px;line-height:14px;color:var(--grey-text)}

/* info cards */
.info-card{top:560px;width:196px;height:105px;background:linear-gradient(#8a8a8a 30%,var(--card-dark))}
.info-card .band{position:absolute;left:0;top:0;width:196px;height:38px;background:linear-gradient(90deg,#f7dc70 0,#e7b938 60%,#d9a520)}
.info-card .badge{position:absolute;left:-2px;top:-10px;width:54px;height:48px;border-radius:0 0 28px 0;background:#fff}
.info-card .k1{position:absolute;left:62px;top:9px;font-size:10px;font-weight:600;color:#fff}
.info-card .k2{position:absolute;right:8px;top:20px;font-size:13px;font-weight:700;color:#fff;text-transform:uppercase}
.info-card .date{position:absolute;left:14px;top:44px;font-size:8px;font-style:italic;color:#fff}
.info-card .copy{position:absolute;left:14px;width:172px;font-size:8px;line-height:11px;color:#fff}
.info-card .go{position:absolute;right:-2px;bottom:-6px;width:24px;height:24px;border-radius:50%;background:#fff;box-shadow:0 1px 3px rgba(0,0,0,.4)}
.card-shadow{top:668px;width:160px;height:12px;background:radial-gradient(ellipse at 50% 0,rgba(0,0,0,.15),transparent 70%)}
.avatars{position:absolute;left:44px;top:39px;display:flex;gap:3px}
.avatars i{display:block;width:19px;height:16px;background:linear-gradient(#e2c6a0,#a87c58)}

/* featured */
.featured-bar{left:126px;top:690px;width:631px;height:31px;border:1px solid #ddd;background:linear-gradient(#fff,#f3f3f3)}
.featured-bar h2{position:absolute;left:12px;top:6px;font-size:13px;font-weight:700;color:#333}
.pager{top:4px;width:20px;height:22px;border:1px solid #aab;background:#eef0f4}
.product{top:731px;width:143px}
.product .shot{position:relative;width:143px;height:125px;border:1px solid #ddd;box-shadow:0 1px 3px rgba(0,0,0,.12);background:#fff;overflow:hidden}
.product .shot div{position:absolute;left:16px;top:50px;width:110px;height:26px;border-radius:50%}
.stars{position:absolute;left:2px;top:130px;display:flex;gap:1px}
.product h3{position:absolute;left:2px;top:145px;font-size:11px;font-weight:700;color:var(--red)}
.product .desc{position:absolute;left:3px;top:161px;width:145px;font-size:7.5px;line-height:11px;color:#222}
.product .price{position:absolute;left:3px;top:187px;font-size:11.5px;font-weight:700}
.btn-cart{position:absolute;left:0;top:211px;width:76px;height:18px;background:#222;border-radius:2px;color:#fff;font-size:7px;font-weight:700;line-height:18px;padding-left:26px}
.btn-cart svg{position:absolute;left:7px;top:4px}
.mini{position:absolute;top:211px;width:18px;height:18px;border:1px solid #bbb;background:#fff}

/* footer */
.site-footer{left:0;top:978px;width:884px;height:187px;background:var(--footer)}
.foot-nav{left:126px;top:38px;font-family:'Josefin Slab',serif;font-size:10px;color:var(--footer-text);display:flex}
.foot-nav span{padding:0 7px;border-left:1px solid #444}
.foot-nav span:first-child{padding-left:0;border:none}
.contact-line{font-family:'Questrial',sans-serif;font-size:10px;color:#6a6a6a;display:flex;align-items:center;gap:5px}
.copyright{left:126px;top:132px;font-size:7px;color:#6a6a6a}
.copyright b{font-weight:400;color:#fff}
.newsletter-title{left:544px;top:36px;font-family:'Questrial',sans-serif;font-size:9.5px;letter-spacing:1.8px;color:#ccc}
.newsletter-title span{font-family:'Josefin Slab',serif;font-size:15px;letter-spacing:0;color:#fff;margin-left:4px}
.field{left:530px;width:221px;height:25px;background:var(--footer-field);color:#ddd;font-family:'Questrial',sans-serif;font-size:10px;letter-spacing:1.5px;text-align:center;line-height:25px}
.subscribe{left:530px;top:124px;width:219px;height:29px;background:#fff;color:#222;font-family:'Questrial',sans-serif;font-size:10px;letter-spacing:2px;text-align:center;line-height:29px}
</style>
</head>
<body>

<header class="abs site-header">
  <div class="abs brand"><div class="l1">CREST HORN</div><div class="l2">INSTRUMENTS</div></div>
  <nav class="nav">
    <a style="left:164px">Home</a><a style="left:229px">Courses</a><a style="left:306px">Facilities</a>
    <a style="left:557px">News</a><a style="left:617px">Events</a><a style="left:685px">Contact</a>
  </nav>
  <div class="abs account">Login &nbsp;|&nbsp; Register</div>
  <svg class="abs cart-icon" width="56" height="22" viewBox="0 0 56 22">
    <path d="M1 6h4l3 9h10l2-7H7" fill="none" stroke="#fff" stroke-width="2"/>
    <circle cx="10" cy="18" r="1.6" fill="#fff"/><circle cx="17" cy="18" r="1.6" fill="#fff"/>
    <circle cx="21" cy="5" r="5" fill="#666"/><text x="21" y="8" font-size="7" fill="#fff" text-anchor="middle" font-family="Open Sans,sans-serif">0</text>
    <text x="35" y="13" font-size="10" fill="#fff" font-family="Open Sans,sans-serif">$</text>
    <path d="M45 9l2.5 2.5L50 9" fill="none" stroke="#fff"/>
  </svg>
</header>

<div class="abs hero-side left" role="img" aria-label="Soft grey smoke wisps"></div>
<div class="abs hero-side right" role="img" aria-label="Soft grey smoke wisps"></div>
<div class="abs hero-photo" role="img" aria-label="Black and white photo of a trumpet player beside a violinist playing"></div>
<div class="abs hero-shadow"></div>
<div class="abs slider-arrow" style="left:90px;top:194px"><svg width="26" height="26"><path d="M15 7l-6 6 6 6" fill="none" stroke="#5a4200" stroke-width="2.5"/></svg></div>
<div class="abs slider-arrow" style="left:766px;top:194px"><svg width="26" height="26"><path d="M11 7l6 6-6 6" fill="none" stroke="#5a4200" stroke-width="2.5"/></svg></div>

<section class="abs welcome">
  <h1>WELCOME TO <span>CRESTHORN INSTRUMENTS</span></h1>
  <!-- microphone -->
  <div class="abs feature-circle" style="left:152px;top:51px"><svg width="72" height="72"><rect x="30" y="18" width="12" height="22" rx="6" fill="var(--icon-light)"/><path d="M25 33a11 11 0 0 0 22 0M36 44v9M29 53h14" fill="none" stroke="var(--icon-light)" stroke-width="2.5" stroke-linecap="round"/></svg></div>
  <!-- saxophone -->
  <div class="abs feature-circle" style="left:280px;top:51px"><svg width="72" height="72"><path d="M44 14l-3 2 1 2" fill="none" stroke="var(--icon-light)" stroke-width="2.5" stroke-linecap="round"/><path d="M41 18c-1 6 0 14-1 24 0 6-3 10-8 10s-8-4-7-8l2-6h5l-1 5c0 2 1 3 2 3s3-1 3-4c1-8 0-16 1-24z" fill="var(--icon-light)"/><path d="M24 40c-3-1-4 1-3 3" fill="none" stroke="var(--icon-light)" stroke-width="3"/><g fill="var(--icon-grey)"><circle cx="39" cy="26" r="1.2"/><circle cx="39" cy="32" r="1.2"/><circle cx="38.6" cy="38" r="1.2"/></g></svg></div>
  <!-- notes -->
  <div class="abs feature-circle" style="left:411px;top:51px"><svg width="72" height="72"><path d="M31 46V22l16-4v24" fill="none" stroke="var(--icon-light)" stroke-width="2.5"/><path d="M31 26l16-4" stroke="var(--icon-light)" stroke-width="4"/><ellipse cx="27" cy="46" rx="5" ry="4" fill="var(--icon-light)"/><ellipse cx="43" cy="42" rx="5" ry="4" fill="var(--icon-light)"/></svg></div>
  <!-- guitar -->
  <div class="abs feature-circle" style="left:542px;top:51px"><svg width="72" height="72"><path d="M38 30l10-10" stroke="var(--icon-light)" stroke-width="3.5" stroke-linecap="round"/><path d="M47 17l5 5-3 2-4-4z" fill="var(--icon-light)"/><path d="M35 28c3 1 6 4 6 7-1 3-3 3-4 5 0 5-5 10-11 9-5-1-7-6-5-11 1-4 5-4 7-6 1-2 3-5 7-4z" fill="var(--icon-light)"/><circle cx="31" cy="39" r="3" fill="var(--icon-grey)"/></svg></div>
  <!-- keyboard -->
  <div class="abs feature-circle" style="left:674px;top:51px"><svg width="72" height="72"><rect x="14" y="24" width="44" height="24" fill="var(--icon-light)"/><g stroke="var(--icon-grey)" stroke-width="1"><path d="M19.5 24v24M25 24v24M30.5 24v24M36 24v24M41.5 24v24M47 24v24M52.5 24v24"/></g><g fill="var(--icon-grey)"><rect x="17.5" y="24" width="4" height="14"/><rect x="23" y="24" width="4" height="14"/><rect x="34" y="24" width="4" height="14"/><rect x="39.5" y="24" width="4" height="14"/><rect x="45" y="24" width="4" height="14"/></g></svg></div>
  <p>Lorem ipsum dolor sit amet, consectetuer adipiscing elit, sed diam nonummy nibh euismod tincidunt ut laoreet dolore magna aliquam erat volutpat. Ut wisi enim ad minim veniam, quis nostrud exerci tation ullamcorper</p>
</section>

<article class="abs info-card" style="left:128px">
  <div class="band"></div><div class="badge"></div>
  <svg class="abs" style="left:8px;top:-3px" width="32" height="34"><path d="M10 8l18-5v20" fill="none" stroke="#111" stroke-width="3"/><path d="M10 8v18" stroke="#111" stroke-width="3"/><path d="M10 10l18-5" stroke="#111" stroke-width="5"/><ellipse cx="7" cy="26" rx="4.5" ry="3.5" fill="#111"/><ellipse cx="25" cy="23" rx="4.5" ry="3.5" fill="#111"/></svg>
  <div class="k1">Music News &amp;</div><div class="k2">Events</div>
  <div class="date">23-Jun-2014</div>
  <div class="copy" style="top:57px">Nulla egestas mi non pulvinar sodales. Vesti bulum id luctus augue. Integer sem nisl, susc ipit sit amet cursus non, venenatis</div>
  <div class="go"><svg width="24" height="24"><path d="M7 10h5V7l5 5-5 5v-3H7z" fill="var(--red)"/></svg></div>
</article>
<article class="abs info-card" style="left:346px">
  <div class="band"></div><div class="badge"></div>
  <svg class="abs" style="left:4px;top:-4px" width="40" height="36"><path d="M20 17l14-12" stroke="#111" stroke-width="3" stroke-linecap="round"/><path d="M32 3l5 4-3 2-4-3z" fill="#111"/><path d="M17 14c3 1 6 3 5 6-1 2-3 2-3 4-1 5-6 9-11 7-4-2-5-6-3-10 1-3 5-3 7-5 1-1 2-3 5-2z" fill="#111"/><circle cx="13" cy="23" r="2.2" fill="#fff"/></svg>
  <div class="k1">Music Teachers</div><div class="k2">Available</div>
  <div class="avatars" role="img" aria-label="Row of teacher portraits"><i></i><i></i><i></i><i></i><i></i></div>
  <div class="copy" style="top:60px">Nulla egestas mi non pulvinar sodales. Vesti bulum id luctus augue. Integer sem nisl, susc ipit sit amet cursus non, venenatis</div>
  <div class="go"><svg width="24" height="24"><path d="M7 10h5V7l5 5-5 5v-3H7z" fill="var(--red)"/></svg></div>
</article>
<article class="abs info-card" style="left:564px">
  <div class="band"></div><div class="badge"></div>
  <svg class="abs" style="left:12px;top:-10px" width="26" height="46"><circle cx="11" cy="9" r="8" fill="#111"/><path d="M7 17h8l-1 5h-6z" fill="#111"/><path d="M11 22v12a5 5 0 0 0 10 0v-8" fill="none" stroke="#111" stroke-width="3" stroke-linecap="round"/><g stroke="#fff" stroke-width=".8"><path d="M5 7h12M4 11h14"/></g></svg>
  <div class="k1">Music Products</div><div class="k2">Highlights</div>
  <div class="copy" style="top:46px">Nulla egestas mi non pulvinar sodales. Vesti bulum id luctus augue. Integer sem nisl, susc ipit sit amet cursus non, venenatis Praesent aliquet mauris ante,</div>
  <div class="go"><svg width="24" height="24"><path d="M7 10h5V7l5 5-5 5v-3H7z" fill="var(--red)"/></svg></div>
</article>
<div class="abs card-shadow" style="left:146px"></div>
<div class="abs card-shadow" style="left:364px"></div>
<div class="abs card-shadow" style="left:582px"></div>

<div class="abs featured-bar">
  <h2>FEATURED PRODUCTS</h2>
  <div class="abs pager" style="left:583px"><svg width="18" height="20"><path d="M14 10H5m4-4l-4 4 4 4" fill="none" stroke="#666" stroke-width="2"/></svg></div>
  <div class="abs pager" style="left:606px"><svg width="18" height="20"><path d="M4 10h9m-4-4l4 4-4 4" fill="none" stroke="#666" stroke-width="2"/></svg></div>
</div>

<svg width="0" height="0" style="position:absolute">
  <defs>
    <path id="star" d="M6 .8l1.5 3.4 3.7.3-2.8 2.4.9 3.6L6 8.6 2.7 10.5l.9-3.6L.8 4.5l3.7-.3z"/>
  </defs>
</svg>

<div class="abs product" style="left:126px">
  <div class="shot"><div role="img" aria-label="Brass alto saxophone with black strap" style="transform:rotate(-65deg);background:radial-gradient(ellipse,rgba(200,160,60,.75),rgba(230,200,120,.3) 55%,rgba(255,255,255,0) 72%)"></div></div>
  <div class="stars"><svg width="12" height="12"><use href="#star" fill="var(--star)"/></svg><svg width="12" height="12"><use href="#star" fill="var(--star)"/></svg><svg width="12" height="12"><use href="#star" fill="var(--star)"/></svg><svg width="12" height="12"><use href="#star" fill="none" stroke="var(--star)"/></svg><svg width="12" height="12"><use href="#star" fill="none" stroke="var(--star)"/></svg></div>
  <h3>Alto Sax</h3>
  <p class="desc">vitae adipiscing urna accumsan vitae. Nunc varius nunc ut nisl</p>
  <div class="price">$249.99</div>
  <div class="btn-cart"><svg width="14" height="11"><path d="M0 1h3l2 6h7l1.5-5H4" fill="none" stroke="var(--red)" stroke-width="1.6"/><circle cx="6" cy="9.5" r="1.2" fill="var(--red)"/><circle cx="11" cy="9.5" r="1.2" fill="var(--red)"/></svg>Add to Cart</div>
  <div class="mini" style="left:80px"><svg width="16" height="16"><g fill="#3a9a3a"><rect x="4" y="10" width="1.6" height="2"/><rect x="6.5" y="8.5" width="1.6" height="3.5"/><rect x="9" y="7" width="1.6" height="5"/><rect x="11.5" y="5" width="1.6" height="7"/></g></svg></div>
  <div class="mini" style="left:102px"><svg width="16" height="16"><g transform="translate(2 2)"><use href="#star" fill="none" stroke="#3a9a3a"/></g></svg></div>
</div>
<div class="abs product" style="left:289px">
  <div class="shot"><div role="img" aria-label="Brass trombone" style="transform:rotate(-50deg);width:130px;left:6px;background:radial-gradient(ellipse,rgba(190,170,100,.7),rgba(220,205,150,.3) 55%,rgba(255,255,255,0) 72%)"></div></div>
  <div class="stars"><svg width="12" height="12"><use href="#star" fill="var(--star)"/></svg><svg width="12" height="12"><use href="#star" fill="var(--star)"/></svg><svg width="12" height="12"><use href="#star" fill="var(--star)"/></svg><svg width="12" height="12"><use href="#star" fill="none" stroke="var(--star)"/></svg><svg width="12" height="12"><use href="#star" fill="none" stroke="var(--star)"/></svg></div>
  <h3>Trombone</h3>
  <p class="desc">vitae adipiscing urna accumsan vitae. Nunc varius nunc ut nisl</p>
  <div class="price">$249.99</div>
  <div class="btn-cart"><svg width="14" height="11"><path d="M0 1h3l2 6h7l1.5-5H4" fill="none" stroke="var(--red)" stroke-width="1.6"/><circle cx="6" cy="9.5" r="1.2" fill="var(--red)"/><circle cx="11" cy="9.5" r="1.2" fill="var(--red)"/></svg>Add to Cart</div>
  <div class="mini" style="left:80px"><svg width="16" height="16"><g fill="#3a9a3a"><rect x="4" y="10" width="1.6" height="2"/><rect x="6.5" y="8.5" width="1.6" height="3.5"/><rect x="9" y="7" width="1.6" height="5"/><rect x="11.5" y="5" width="1.6" height="7"/></g></svg></div>
  <div class="mini" style="left:102px"><svg width="16" height="16"><g transform="translate(2 2)"><use href="#star" fill="none" stroke="#3a9a3a"/></g></svg></div>
</div>
<div class="abs product" style="left:452px">
  <div class="shot"><div role="img" aria-label="Black clarinet with silver keys" style="transform:rotate(35deg);width:130px;height:20px;left:6px;top:52px;background:radial-gradient(ellipse,rgba(30,30,30,.85),rgba(80,80,80,.35) 55%,rgba(255,255,255,0) 72%)"></div></div>
  <div class="stars"><svg width="12" height="12"><use href="#star" fill="var(--star)"/></svg><svg width="12" height="12"><use href="#star" fill="var(--star)"/></svg><svg width="12" height="12"><use href="#star" fill="var(--star)"/></svg><svg width="12" height="12"><use href="#star" fill="none" stroke="var(--star)"/></svg><svg width="12" height="12"><use href="#star" fill="none" stroke="var(--star)"/></svg></div>
  <h3>Clarinet</h3>
  <p class="desc">vitae adipiscing urna accumsan vitae. Nunc varius nunc ut nisl</p>
  <div class="price">$249.99</div>
  <div class="btn-cart"><svg width="14" height="11"><path d="M0 1h3l2 6h7l1.5-5H4" fill="none" stroke="var(--red)" stroke-width="1.6"/><circle cx="6" cy="9.5" r="1.2" fill="var(--red)"/><circle cx="11" cy="9.5" r="1.2" fill="var(--red)"/></svg>Add to Cart</div>
  <div class="mini" style="left:80px"><svg width="16" height="16"><g fill="#3a9a3a"><rect x="4" y="10" width="1.6" height="2"/><rect x="6.5" y="8.5" width="1.6" height="3.5"/><rect x="9" y="7" width="1.6" height="5"/><rect x="11.5" y="5" width="1.6" height="7"/></g></svg></div>
  <div class="mini" style="left:102px"><svg width="16" height="16"><g transform="translate(2 2)"><use href="#star" fill="none" stroke="#3a9a3a"/></g></svg></div>
</div>
<div class="abs product" style="left:615px">
  <div class="shot"><div role="img" aria-label="Cream coloured recorder flute" style="transform:rotate(-48deg);width:130px;height:20px;left:6px;top:52px;background:radial-gradient(ellipse,rgba(215,205,170,.9),rgba(230,222,195,.4) 55%,rgba(255,255,255,0) 72%)"></div></div>
  <div class="stars"><svg width="12" height="12"><use href="#star" fill="var(--star)"/></svg><svg width="12" height="12"><use href="#star" fill="var(--star)"/></svg><svg width="12" height="12"><use href="#star" fill="var(--star)"/></svg><svg width="12" height="12"><use href="#star" fill="none" stroke="var(--star)"/></svg><svg width="12" height="12"><use href="#star" fill="none" stroke="var(--star)"/></svg></div>
  <h3>Flute</h3>
  <p class="desc">vitae adipiscing urna accumsan vitae. Nunc varius nunc ut nisl</p>
  <div class="price">$249.99</div>
  <div class="btn-cart"><svg width="14" height="11"><path d="M0 1h3l2 6h7l1.5-5H4" fill="none" stroke="var(--red)" stroke-width="1.6"/><circle cx="6" cy="9.5" r="1.2" fill="var(--red)"/><circle cx="11" cy="9.5" r="1.2" fill="var(--red)"/></svg>Add to Cart</div>
  <div class="mini" style="left:80px"><svg width="16" height="16"><g fill="#3a9a3a"><rect x="4" y="10" width="1.6" height="2"/><rect x="6.5" y="8.5" width="1.6" height="3.5"/><rect x="9" y="7" width="1.6" height="5"/><rect x="11.5" y="5" width="1.6" height="7"/></g></svg></div>
  <div class="mini" style="left:102px"><svg width="16" height="16"><g transform="translate(2 2)"><use href="#star" fill="none" stroke="#3a9a3a"/></g></svg></div>
</div>

<footer class="abs site-footer">
  <div class="abs foot-nav"><span>HOME</span><span>ABOUT</span><span>FEATURES</span><span>BLOG</span><span>CONTACT</span></div>
  <div class="abs contact-line" style="left:126px;top:73px"><svg width="18" height="18"><circle cx="9" cy="9" r="9" fill="#555"/><rect x="4" y="6" width="10" height="7" fill="none" stroke="#222" stroke-width="1.2"/><path d="M4 6l5 4 5-4" fill="none" stroke="#222" stroke-width="1.2"/></svg>info@cresthorn.com</div>
  <div class="abs contact-line" style="left:257px;top:73px"><svg width="18" height="18"><circle cx="9" cy="9" r="9" fill="#555"/><path d="M6 4l2 3-1 1.5c.7 1.5 1.8 2.6 3.3 3.3L12 10.8l3 2-1 1.7C9 14.5 4 9.5 4.3 5z" fill="#222"/></svg>555-010-2040</div>
  <div class="abs copyright">Copyright © 2014 All Right Reserved <b>CRESTHORNSUPPLY.COM</b></div>
  <div class="abs newsletter-title">Sign up for our<span>Newsletter</span></div>
  <div class="abs field" style="top:62px">Name</div>
  <div class="abs field" style="top:93px">Email</div>
  <div class="abs subscribe">Subscribe</div>
</footer>

</body>
</html>
```